Audio Tour Poster

I need a poster to show information on a audio tour ... walk ... bike etc ... the poster needs to be generic so that it could be used for several projects ... a space needs to be left to add a tour title and another area where a tri fold brochure can be placed for people to access ... the tri fold poster will be based on 8.5 x 14 inch legal size ...

The size of the final poster will be 18x 24 inches ... an example of a audio tour can be found at
http://trallexo.com/walk/568 or http://trallexo.com/walk/2507

Industry/Entity Type

Legal

```html
<!DOCTYPE html>
<html lang="en">
<head>
<meta charset="utf-8">
<title>Audio Tour Poster</title>
<link rel="stylesheet" href="https://fonts.googleapis.com/css2?family=Courgette&family=Indie+Flower&display=swap">
<style>
  :root {
    --bg-light: #c3bcba;
    --bg-mid: #aaa2a0;
    --bg-dark: #6e6462;
    --grunge: rgba(92, 72, 64, 0.22);
    --tag-paper: #e4cf9e;
    --tag-edge: #c9b27e;
    --tag-fold: #d8c08a;
    --ink-brown: #57361b;
    --note-paper: #ddd3a3;
    --note-line: #a8b4a6;
    --note-ink: #2f2a22;
    --frame-cream: #e9e3c8;
    --frame-shade: #c4bb98;
    --slot-grey: #7b7270;
    --slot-text: #f3f0ea;
    --tile-shadow: rgba(0, 0, 0, 0.45);
  }
  * { box-sizing: border-box; margin: 0; padding: 0; }
  html, body { width: 905px; height: 1200px; overflow: hidden; background: var(--bg-mid); }

  .poster {
    position: relative; width: 905px; height: 1200px; overflow: hidden;
    background: radial-gradient(ellipse 75% 70% at 48% 42%, var(--bg-light) 0%, var(--bg-mid) 60%, var(--bg-dark) 100%);
  }

  .grunge-texture {
    position: absolute; border-radius: 50%;
    background: radial-gradient(ellipse at center, var(--grunge) 0%, transparent 70%);
  }
  .grunge-texture--top { left: 120px; top: -60px; width: 480px; height: 160px; }
  .grunge-texture--track { left: 560px; top: 260px; width: 300px; height: 520px; transform: rotate(-28deg); }

  /* Photo tiles */
  .photo {
    position: absolute; border-radius: 14px;
    transform: translate(-50%, -50%) rotate(10deg);
    box-shadow: 3px 6px 12px var(--tile-shadow);
  }
  .photo--church  { left: 358px; top: 60px;   width: 110px; height: 100px; background: linear-gradient(#86acd8 0%, #c9d6e4 35%, #b39259 70%, #8a6c3c 100%); }
  .photo--facades { left: 112px; top: 200px;  width: 248px; height: 350px; background: linear-gradient(100deg, #e6e6e6 0%, #c9c9c9 30%, #b2302c 55%, #2d4fa8 85%, #3a5fbf 100%); }
  .photo--stairs  { left: 44px;  top: 506px;  width: 170px; height: 160px; background: linear-gradient(#4a443e, #1a1714); }
  .photo--pagoda  { left: 346px; top: 236px;  width: 232px; height: 190px; background: linear-gradient(135deg, #7e1c18 0%, #35602a 38%, #24401c 100%); }
  .photo--garden  { left: 518px; top: 326px;  width: 138px; height: 126px; background: linear-gradient(135deg, #4b7a34 0%, #2a4a1e 60%, #8a3a2a 100%); }
  .photo--harbour { left: 333px; top: 518px;  width: 384px; height: 340px; background: linear-gradient(#9cc0d6 0%, #b6cad2 28%, #b98a5a 45%, #8a6a48 60%, #2a2620 75%, #1a2230 100%); }
  .photo--doorway { left: 640px; top: 544px;  width: 207px; height: 186px; background: linear-gradient(135deg, #d9c9a4 0%, #b5a37c 60%, #5e533e 100%); }
  .photo--skyline { left: 106px; top: 680px;  width: 250px; height: 124px; background: linear-gradient(#0e1424 0%, #1f2c52 65%, #b8923e 85%, #1a1f30 100%); }
  .photo--roofs   { left: 96px;  top: 832px;  width: 200px; height: 178px; background: linear-gradient(135deg, #2e2622 0%, #3c302a 35%, #b5532c 55%, #d9b08a 100%); }
  .photo--oldtown { left: 336px; top: 802px;  width: 205px; height: 190px; background: linear-gradient(#a7bfd6 0%, #8e9aa2 40%, #8a5e44 65%, #5c3a2a 100%); }
  .photo--desert  { left: 82px;  top: 1036px; width: 120px; height: 184px; background: linear-gradient(#7ea9de 0%, #cfd9e4 30%, #d8b48a 50%, #c38d5c 100%); }

  /* Title tag */
  .title-tag {
    position: absolute; left: 484px; top: 62px; width: 440px; height: 240px;
    transform: rotate(-3deg);
  }
  .title-tag svg { position: absolute; inset: 0; }
  .title-tag__heading {
    position: absolute; left: 88px; top: 64px;
    font-family: "Courgette", cursive; font-size: 50px; line-height: 1;
    color: var(--ink-brown); transform: rotate(-4deg); white-space: nowrap;
  }
  .title-tag__sub {
    position: absolute; left: 104px; top: 128px;
    font-family: "Indie Flower", cursive; font-size: 24px; line-height: 1;
    color: var(--ink-brown); transform: rotate(-4deg); white-space: nowrap;
  }

  /* Event note */
  .event-note {
    position: absolute; left: 122px; top: 872px; width: 430px; height: 360px;
    transform: rotate(-3deg);
    background:
      repeating-linear-gradient(to bottom, transparent 0 30px, var(--note-line) 30px 31px) 0 44px / 100% 100% no-repeat,
      var(--note-paper);
    box-shadow: 3px 6px 12px rgba(0, 0, 0, 0.35);
    border-radius: 4px;
  }
  .event-note__hole {
    position: absolute; top: 22px; width: 20px; height: 20px; border-radius: 50%;
    background: var(--bg-mid);
  }
  .event-note__hole--first { left: 80px; }
  .event-note__hole--second { left: 172px; }
  .event-note__text {
    position: absolute; left: 108px; top: 198px;
    font-family: "Indie Flower", cursive; font-size: 24px; line-height: 1.05;
    color: var(--note-ink); transform: rotate(-4deg); white-space: nowrap;
  }

  /* Brochure holder */
  .brochure-slot { position: absolute; left: 584px; top: 668px; width: 280px; height: 480px; }
  .brochure-slot svg { position: absolute; inset: 0; overflow: visible; }
  .brochure-slot__text {
    position: absolute; left: 48px; top: 202px;
    font-family: "Indie Flower", cursive; font-size: 23px; line-height: 1.05;
    color: var(--slot-text); transform: rotate(-6deg); white-space: nowrap;
  }
</style>
</head>
<body>
<div class="poster">
  <div class="grunge-texture grunge-texture--top" role="img" aria-label="Faint grunge texture"></div>
  <div class="grunge-texture grunge-texture--track" role="img" aria-label="Faint tyre track texture"></div>

  <div class="event-note">
    <span class="event-note__hole event-note__hole--first"></span>
    <span class="event-note__hole event-note__hole--second"></span>
    <div class="event-note__text">Area for description<br>and details of event</div>
  </div>

  <div class="photo photo--church" role="img" aria-label="Photo of a church tower against blue sky"></div>
  <div class="photo photo--facades" role="img" aria-label="Photo of white and red apartment facades"></div>
  <div class="photo photo--stairs" role="img" aria-label="Photo of dark stone steps"></div>
  <div class="photo photo--pagoda" role="img" aria-label="Photo of a red pagoda in a green garden"></div>
  <div class="photo photo--garden" role="img" aria-label="Photo of a lush garden"></div>
  <div class="photo photo--skyline" role="img" aria-label="Photo of a city skyline at night"></div>
  <div class="photo photo--harbour" role="img" aria-label="Photo of an old walled town by the water"></div>
  <div class="photo photo--doorway" role="img" aria-label="Photo of a stone house doorway"></div>
  <div class="photo photo--roofs" role="img" aria-label="Photo of red tiled rooftops"></div>
  <div class="photo photo--oldtown" role="img" aria-label="Photo of an old town with a spire"></div>
  <div class="photo photo--desert" role="img" aria-label="Photo of a cyclist on a sandy trail"></div>

  <div class="title-tag">
    <svg width="440" height="240" viewBox="0 0 440 240">
      <path d="M10 56 L58 22 L352 18 L420 78 L428 220 L22 232 Z" fill="var(--tag-paper)" stroke="var(--tag-edge)" stroke-width="2"/>
      <path d="M352 18 C372 20 396 34 420 78 C400 66 384 62 366 64 C360 46 356 30 352 18 Z" fill="var(--tag-fold)"/>
      <circle cx="38" cy="114" r="8" fill="var(--bg-mid)"/>
    </svg>
    <div class="title-tag__heading">Audio Tour</div>
    <div class="title-tag__sub">title tour description</div>
  </div>

  <div class="brochure-slot">
    <svg width="280" height="480" viewBox="0 0 280 480">
      <!-- frame bands -->
      <path d="M94 0 L266 0 Q276 0 276 10 L276 468 Q276 478 266 478 L10 478 Q0 478 0 468 L0 168 L20 168 L20 442 L256 442 L256 34 L94 34 Z"
            fill="var(--frame-cream)" opacity="0.92"/>
      <!-- slot area -->
      <rect x="20" y="34" width="236" height="408" fill="var(--slot-grey)"/>
      <rect x="20" y="34" width="236" height="408" fill="none" stroke="var(--frame-shade)" stroke-width="3"/>
      <rect x="1" y="1" width="274" height="476" rx="10" fill="none" stroke="var(--frame-shade)" stroke-width="1.5" opacity="0.7"/>
      <!-- peeled ribbon -->
      <path d="M94 0 C70 4 56 18 52 34 C48 52 40 60 28 72 C14 86 10 100 14 116 C18 132 8 148 0 168 L20 168 C26 150 34 136 30 118 C26 104 30 94 42 84 C58 70 66 56 70 40 C74 28 82 30 94 34 Z"
            fill="var(--frame-cream)" stroke="var(--frame-shade)" stroke-width="1.5"/>
      <path d="M52 34 C48 52 40 60 28 72 L42 84 C58 70 66 56 70 40 Z" fill="var(--frame-shade)" opacity="0.7"/>
      <path d="M14 116 C18 132 8 148 0 168 L8 168 C14 150 22 136 20 118 Z" fill="var(--frame-shade)" opacity="0.5"/>
    </svg>
    <div class="brochure-slot__text">Area for tri-fold<br>8.5 x 24 Brochure</div>
  </div>
</div>
</body>
</html>
```